南谷 睦月というペンネームで活動しているものです。

本業は組織・人財開発領域に特化した支援を行う会社において、
企画の提案、プロジェクトマネジメント、依頼後の進捗管理など、
お客様の中に自身も入りながら、経営を変えていくような支援を行っています。

ご依頼をさせていただく表紙デザインですが、
9月16日にPagoraにて、下記の内容を発行いたしました。
============================
現場を変える人が大切にする4つの視点:
~挑戦した人々の物語から静かに学び取る~

www.bookvale-store.jp/item/Q72KD4MX3N
こちらの内容について、発行に向けた表紙手配が間に合わなかったこともあり、
一旦はデザインを自身で考え、発行をいたしましたが、
表紙は書籍の顔ということもあり、作成依頼を進めることに決めました。

デザイン制作にあたって検討いただきたいのは下記2点です。

検討に当たってのポイントは下記2点です。
① 悩みに対しての答えが見つかるような印象を持てる
② あまり複雑すぎないデザインであること

① 悩みに対しての答えが見つかるような印象を持てる
・取り上げたPagoraでは、スキル・ノウハウ本ではなく、
実践されている方が直面されたエピソードをもとにして、
悩みを解決するためのヒントを取り上げています。
そのようなニュアンスが感じられるようなデザインに期待です。

② あまり複雑なデザインではないこと
・凝ったデザインよりは、わかりやすいデザインを好む方です。
複雑なカラーよりは、色を限りながらも、与えられた題材に対しての
表現を頂けるようなデザインが好みではあります。
※ が、良いものが出てくれば、それ限りではございませんので、
あくまで、現時点の好みとしてお伝えを致します

最終的に今回のコンペでは「R_hoshidaさん」のデザインを採用させて頂きます。
重視した点は改めて、下記の2点がベースとなります。
① 悩みに対しての答えが見つかるような印象を持てる
② あまり複雑なデザインではないこと
絵で①のイメージを喚起しつつ、今回の書籍で押し出していることを文字で強調いただく構成となっており、②の点からも適切と考えて採択をさせて頂きました。

改めて、この度はご提案をいただきましてありがとうございます。

引き続き、個人的な目標としては3か月~6か月に1回の頻度で、
Pagora向けの発行物を執筆していく予定です。
また、このような形でご支援の相談をさせていただきますので、
よろしければ是非、お力添えをどうぞお願い申し上げます。

```html
<!DOCTYPE html>
<html lang="ja">
<head>
<meta charset="utf-8">
<title>現場を変える人が大切にする4つの視点</title>
<link rel="stylesheet" href="https://fonts.googleapis.com/css2?family=Noto+Sans+JP:wght@500;700;900&family=Bodoni+Moda:opsz,wght@6..96,700&family=Noto+Serif:ital@1&display=swap">
<style>
  :root {
    --paper: #ffffff;
    --ink-navy: #1d2b63;
    --ink-blue: #1f5bb0;
    --accent-yellow: #fbe73a;
    --figure-blue: #8fd0ee;
    --muted: #7a7a7a;
    --text-dark: #1a1a1a;
  }
  html, body { margin: 0; padding: 0; overflow: hidden; background: var(--paper); }
  .cover {
    position: relative;
    width: 750px; height: 1200px;
    overflow: hidden;
    background: var(--paper);
    font-family: "Noto Sans JP", sans-serif;
  }
  .burst { position: absolute; left: 0; top: 0; width: 750px; height: 1200px; }
  .burst polygon { fill: var(--accent-yellow); }
  .lead {
    position: absolute; left: 32px; top: 26px; margin: 0;
    color: var(--ink-blue); font-weight: 900; font-size: 42px; line-height: 54px;
    letter-spacing: 1px;
  }
  .title { margin: 0; color: var(--ink-navy); font-weight: 500; }
  .title-number {
    position: absolute; left: 50px; top: 170px;
    font-family: "Bodoni Moda", serif; font-weight: 700;
    font-variant-numeric: lining-nums;
    font-size: 300px; line-height: 1;
  }
  .title-particle {
    position: absolute; left: 262px; top: 250px;
    font-size: 66px; line-height: 1; letter-spacing: -4px;
  }
  .title-word-a, .title-word-b {
    position: absolute; line-height: 1;
  }
  .title-word-a { left: 250px; top: 305px; font-size: 240px; }
  .title-word-b { left: 430px; top: 440px; font-size: 285px; }
  .runner {
    position: absolute; left: 458px; top: 352px;
    width: 60px; height: 46px; border-radius: 16px;
    background: var(--figure-blue);
  }
  .subtitle {
    position: absolute; left: 295px; top: 735px; margin: 0;
    color: var(--ink-blue); font-weight: 900; font-size: 34px; line-height: 48px;
    letter-spacing: 1px;
  }
  .author { position: absolute; left: 560px; top: 880px; }
  .author-mark { font-size: 16px; color: var(--text-dark); font-weight: 500; }
  .author-name {
    margin: 6px 0 0 22px; font-size: 42px; font-weight: 900;
    color: var(--text-dark); line-height: 1.1;
  }
  .author-roman {
    margin: 6px 0 10px 6px; font-family: "Noto Serif", serif; font-style: italic;
    font-size: 17px; color: var(--muted);
  }
</style>
</head>
<body>
<main class="cover">
  <svg class="burst" viewBox="0 0 750 1200" aria-hidden="true">
    <polygon points="138,455 440,630 378,668 638,830 163,1060 238,745"/>
  </svg>

  <p class="lead">現場を変える人が<br>大切にする</p>

  <h1 class="title">
    <span class="title-number">4</span>
    <span class="title-particle">つの</span>
    <span class="title-word-a">視</span>
    <span class="title-word-b">点</span>
  </h1>

  <div class="runner" role="img" aria-label="走る人物の小さなイラスト"></div>

  <p class="subtitle">挑戦した人々の<br>物語から<br>静かに<br>学び取る</p>

  <div class="author">
    <div class="author-mark">著</div>
    <p class="author-name">南谷</p>
    <p class="author-roman">Minamiya Mutsuki</p>
    <p class="author-name">睦月</p>
  </div>
</main>
</body>
</html>
```